Banner Design for Holistic Clinic

We need a banner to be designed for a Holistic Clinic which treats patient using IV Nutrition therapy, IV Vitamin C therapy, Chelation therapy, Homoepathy , Accupuncture, Ayurveda. Our website is www.verdantcarehub.in

We need the banner to show case all our services. IV Nutrition therapy, IV Vitamin C therapy, Chelation therapy, Homoepathy , Accupuncture, Ayurveda with special emphasis on IV Therapies. This will be in the front of the web page and will be used for leaflets and flex material.Ideally

I like the concept of IV infsuion bags, fruits etc. I have attached some of the pic which i liked. Please see the attachment "banner clinic july 13" But feel free to change it and bring in something better that will showcase all our services together

Target Market(s)

30 plus Adults

Industry/Entity Type

Health And Wellness

Font styles to use
Serif

Colors
acd036
f37122
33a6d7

Requirements
Must have
• Some samples are given below. It got to be colourful, yet pleasing.

```html
<!DOCTYPE html>
<html lang="en">
<head>
<meta charset="utf-8">
<title>Verdant Care Hub – Banner</title>
<link href="https://fonts.googleapis.com/css2?family=Saira+Semi+Condensed:wght@500;700&family=Raleway:ital,wght@0,500;1,500&family=Poppins:wght@600&display=swap" rel="stylesheet">
<style>
  :root {
    --stage: #444444;
    --paper: #ffffff;
    --silk: #eeeff1;
    --brand-green: #1f9a3a;
    --leaf-green: #8cbf26;
    --bar-green: #7fba1f;
    --ink: #1c1c1c;
    --muted: #3a3a3a;
    --pulse-red: #e0262c;
    --citrus: #f7941d;
  }
  * { box-sizing: border-box; margin: 0; padding: 0; }
  html, body { width: 1134px; height: 1200px; overflow: hidden; background: var(--stage); }
  .banner {
    position: absolute; left: 0; top: 348px; width: 1134px; height: 503px; overflow: hidden;
    background:
      radial-gradient(ellipse 420px 260px at 180px 380px, var(--silk), transparent 70%),
      linear-gradient(115deg, #f6f6f7 0%, #ffffff 40%, #f3f3f4 100%);
  }
  .photo { position: absolute; }
  .photo--citrus { left: 0; top: 0; width: 118px; height: 135px;
    background: radial-gradient(circle at 40% 40%, #ffc04d, var(--citrus) 60%, transparent 72%); }
  .photo--ampoules { left: 100px; top: 8px; width: 210px; height: 140px;
    background: linear-gradient(140deg, transparent 20%, #f0e2cf 45%, #d6a66a 55%, transparent 80%); opacity: .8; }
  .photo--citrus-top { left: 215px; top: 0; width: 90px; height: 55px;
    background: radial-gradient(ellipse at 50% 0%, #ffb13b, var(--citrus) 55%, transparent 75%); }
  .photo--drip-bag { left: 997px; top: 0; width: 137px; height: 126px;
    background: radial-gradient(circle at 60% 45%, #d7e96a, #e9c84a 45%, #e6e3d8 70%, transparent 85%); }
  .photo--remedies { left: 754px; top: 117px; width: 380px; height: 386px;
    background:
      radial-gradient(circle at 40% 80%, #cfe3b3, transparent 35%),
      radial-gradient(circle at 55% 40%, #d9d6d0, transparent 45%),
      radial-gradient(circle at 90% 30%, #5a5a5a, transparent 22%),
      linear-gradient(160deg, #f4f3f1, #ebeae7); border-radius: 40% 0 0 0; }

  .identity { position: absolute; left: 280px; top: 40px; }
  .identity__mark { position: absolute; left: 0; top: 30px; width: 96px; height: 96px; background: var(--brand-green); }
  .identity__doctor { position: absolute; left: 139px; top: 0; white-space: nowrap;
    font: 500 16px/1 "Saira Semi Condensed", sans-serif; color: var(--muted); letter-spacing: .5px; }
  .identity__name { position: absolute; left: 139px; top: 24px; white-space: nowrap;
    font: 700 40px/1 "Saira Semi Condensed", sans-serif; color: var(--brand-green); letter-spacing: 1px; }
  .identity__disciplines { position: absolute; left: 139px; top: 72px; white-space: nowrap;
    font: 500 13px/1 "Saira Semi Condensed", sans-serif; color: var(--muted); }
  .identity__rule { position: absolute; left: 139px; top: 93px; width: 434px; height: 2px; background: var(--pulse-red); }

  .tagline { position: absolute; left: 72px; top: 193px; white-space: nowrap;
    font: italic 500 24px/1.2 "Raleway", sans-serif; color: var(--leaf-green); }

  .services { list-style: none; }
  .services li { position: absolute; white-space: nowrap; font: 500 24px/1 "Raleway", sans-serif; color: var(--ink); }
  .services svg { position: absolute; left: -48px; top: -4px; }

  .emphasis { position: absolute; left: 0; top: 404px; width: 698px; height: 63px;
    background: var(--bar-green); border-radius: 0 32px 32px 0; }
  .emphasis p { position: absolute; left: 73px; top: 18px; white-space: nowrap;
    font: 600 24px/1 "Poppins", sans-serif; color: #fff; }
</style>
</head>
<body>
  <section class="banner">
    <div class="photo photo--citrus" role="img" aria-label="Orange slices"></div>
    <div class="photo photo--ampoules" role="img" aria-label="Glass vitamin ampoules"></div>
    <div class="photo photo--citrus-top" role="img" aria-label="Orange slice"></div>
    <div class="photo photo--drip-bag" role="img" aria-label="IV drip bag filled with fruit"></div>
    <div class="photo photo--remedies" role="img" aria-label="Stethoscope, acupuncture needles, herbal mortar, capsules and homeopathic pills"></div>

    <div class="identity">
      <div class="identity__mark"></div>
      <p class="identity__doctor">Dr. Elena Varghese's (MBBS, MD)</p>
      <h1 class="identity__name">VERDANT CARE HUB</h1>
      <p class="identity__disciplines">Allopathy, Ayurveda, Homeopathy, Acupuncture/Sujok</p>
      <div class="identity__rule"></div>
    </div>

    <p class="tagline">An integrative clinic for health Leaving....Naturally!!</p>

    <ul class="services">
      <li style="left:124px;top:258px"><svg width="30" height="30" viewBox="0 0 30 30"><path d="M5 16l7 7L26 7" fill="none" stroke="var(--leaf-green)" stroke-width="4" stroke-linecap="round" stroke-linejoin="round"/></svg>IV NUTRITION THERAPY</li>
      <li style="left:472px;top:258px"><svg width="30" height="30" viewBox="0 0 30 30"><path d="M5 16l7 7L26 7" fill="none" stroke="var(--leaf-green)" stroke-width="4" stroke-linecap="round" stroke-linejoin="round"/></svg>HOMOEPATHY</li>
      <li style="left:124px;top:312px"><svg width="30" height="30" viewBox="0 0 30 30"><path d="M5 16l7 7L26 7" fill="none" stroke="var(--leaf-green)" stroke-width="4" stroke-linecap="round" stroke-linejoin="round"/></svg>IV VITAMIN C THERAPY</li>
      <li style="left:472px;top:312px"><svg width="30" height="30" viewBox="0 0 30 30"><path d="M5 16l7 7L26 7" fill="none" stroke="var(--leaf-green)" stroke-width="4" stroke-linecap="round" stroke-linejoin="round"/></svg>ACCUPUNCTURE</li>
      <li style="left:124px;top:362px"><svg width="30" height="30" viewBox="0 0 30 30"><path d="M5 16l7 7L26 7" fill="none" stroke="var(--leaf-green)" stroke-width="4" stroke-linecap="round" stroke-linejoin="round"/></svg>CHELATION THERAPY</li>
    </ul>

    <div class="emphasis"><p>Ayurveda with Special Emphasis on IV Therapies</p></div>
  </section>
</body>
</html>
```